Short term vacation rental

I need a simple site the we can rent a duplex that is on the sand in Indian rocks beach Fl needs to be able to sync with multiple calendars like tarnivo.com qelm zunt using Wordpress

```html
<!DOCTYPE html>
<html lang="en">
<head>
<meta charset="utf-8">
<title>Sandline Retreats – Indian Rocks Beach Duplex</title>
<link href="https://fonts.googleapis.com/css2?family=Inter:wght@400;500;600&family=Playfair+Display:ital,wght@0,600;0,700;1,500&display=swap" rel="stylesheet">
<style>
:root{
  --navy:#0b5f96;
  --navy-deep:#065e95;
  --ink:#1c1c1c;
  --text:#4a4a4a;
  --muted:#6b6b6b;
  --bg-soft:#f6f6f7;
  --card:#f1f1f3;
  --line:#e4e4e7;
  --chip:#bfeefb;
  --chip-text:#0b5f7a;
  --white:#ffffff;
}
*{box-sizing:border-box;margin:0;padding:0}
html,body{width:1200px;height:2785px;overflow:hidden}
body{font-family:"Inter",sans-serif;color:var(--text);background:var(--white);position:relative}
.serif{font-family:"Playfair Display",serif}
.wrap{width:790px;margin:0 auto;position:relative}

/* nav */
.nav{height:55px;background:var(--white);border-bottom:1px solid var(--line)}
.nav .wrap{display:flex;align-items:center;height:55px}
.brand{display:flex;align-items:center;gap:6px;font-family:"Inter",sans-serif;font-size:11px;font-weight:500;color:#3d6c8a;letter-spacing:.08em}
.brand-dot{width:10px;height:10px;border-radius:50%;background:#9fc3d8}
.nav-links{display:flex;gap:23px;margin-left:154px;font-size:12px;color:#333}
.btn-book{margin-left:auto;background:var(--navy);color:#fff;font-size:12px;font-weight:500;padding:9px 17px;border-radius:20px}

/* hero */
.hero{height:650px;position:relative;background:linear-gradient(180deg,#7a7f93 0%,#b9919c 18%,#e7a88c 33%,#d89f8d 40%,#4a5a72 45%,#2d3d55 60%,#6a6f82 72%,#c9a5a2 82%,#e2b8a7 100%)}
.hero-copy{position:absolute;left:205px;top:222px;width:470px;color:#fff}
.hero h1{font-size:37px;line-height:41px;font-weight:700}
.hero p{margin-top:20px;font-size:13px;line-height:21px}
.hero-btns{display:flex;gap:12px;margin-top:28px}
.btn{font-size:12px;font-weight:500;padding:13px 22px;border-radius:4px}
.btn-primary{background:var(--navy);color:#fff}
.btn-ghost{background:rgba(255,255,255,.18);border:1px solid rgba(255,255,255,.55);color:#fff}

/* experience */
.experience{height:557px;padding-top:34px}
.experience .wrap{display:flex;gap:46px}
.photo-frame{width:395px;height:519px;background:#f0f4f6;border-radius:12px;padding:11px;box-shadow:0 10px 28px rgba(0,0,0,.08)}
.photo-interior{width:373px;height:465px;border-radius:8px;background:linear-gradient(180deg,#c9c2b7 0%,#e3ddd3 20%,#8fd0ea 36%,#1f8fb5 50%,#c8c2b5 62%,#a59a87 100%)}
.exp-text{width:370px;padding-top:24px}
.eyebrow{font-size:11px;letter-spacing:.14em;color:var(--navy);font-weight:500}
.exp-text h2{font-size:28px;line-height:31px;color:var(--ink);margin-top:16px;font-weight:600}
.exp-lead{font-size:13px;line-height:21px;margin-top:22px;color:#444}
.exp-sub{font-size:11.5px;line-height:18px;margin-top:16px;color:#555}
.checks{list-style:none;margin-top:24px}
.checks li{display:flex;align-items:center;gap:9px;font-size:11.5px;font-weight:600;color:var(--ink);height:28px}
.link-floor{display:inline-flex;align-items:center;gap:6px;margin-top:20px;font-size:11.5px;font-weight:600;color:var(--navy);border-bottom:1px solid var(--navy);padding-bottom:3px}

/* curated */
.curated{height:789px;background:var(--bg-soft);padding-top:44px;text-align:center}
.curated h2{font-size:28px;color:var(--ink);font-weight:600}
.curated .intro{font-size:11.5px;line-height:17px;width:530px;margin:12px auto 0;color:#444}
.cards{display:flex;gap:24px;margin-top:47px}
.card{width:247px;height:221px;background:var(--card);border:1px solid var(--line);border-radius:8px;padding:28px 30px 0}
.card-icon{width:44px;height:44px;border-radius:50%;background:var(--navy);margin:0 auto;display:flex;align-items:center;justify-content:center}
.card h3{font-size:12px;font-weight:600;color:var(--ink);margin-top:20px}
.card p{font-size:11px;line-height:17px;margin-top:10px;color:#444}
.testimonial{margin-top:112px}
.testimonial blockquote{font-family:"Playfair Display",serif;font-style:italic;font-weight:500;font-size:18.5px;line-height:24px;color:var(--ink);width:620px;margin:18px auto 0}
.author{display:flex;align-items:center;justify-content:center;gap:10px;margin-top:30px}
.avatar{width:34px;height:34px;border-radius:50%;background:#cde3ee;color:var(--navy);font-size:11px;font-weight:600;display:flex;align-items:center;justify-content:center}
.author-text{text-align:left;font-size:11.5px;line-height:17px;color:#333}

/* local */
.local{height:303px;padding-top:45px}
.local .wrap{display:flex;justify-content:space-between}
.local-text{width:370px;padding-top:12px}
.local h2{font-size:27px;line-height:31px;color:var(--ink);font-weight:600}
.local p{font-size:11.5px;line-height:17px;margin-top:22px;color:#444}
.chips{display:flex;gap:8px;margin-top:14px}
.chip{background:var(--chip);color:var(--chip-text);font-size:9px;font-weight:600;padding:6px 12px;border-radius:12px}
.local-link{display:inline-flex;align-items:center;gap:8px;margin-top:22px;font-size:12px;color:var(--navy)}
.photo-town{width:379px;height:212px;border-radius:12px;background:linear-gradient(180deg,#2f86c8 0%,#6cb4e3 45%,#9cc8a6 62%,#c7ccc8 78%,#3f6f86 100%);box-shadow:0 10px 24px rgba(0,0,0,.15)}

/* cta */
.cta{height:303px;background:var(--navy-deep);text-align:center;color:#fff;padding-top:67px}
.cta h2{font-size:27px;font-weight:600}
.cta p{font-size:11.5px;line-height:17px;width:460px;margin:26px auto 0}
.cta-btns{display:flex;justify-content:center;gap:15px;margin-top:33px}
.btn-light{background:#fff;color:var(--navy);font-size:12px;font-weight:500;padding:16px 29px;border-radius:24px}
.btn-outline{border:1px solid rgba(255,255,255,.7);color:#fff;font-size:12px;font-weight:500;padding:15px 29px;border-radius:24px}

/* footer */
.footer{height:128px;background:var(--bg-soft);padding-top:22px}
.footer .wrap{display:flex;align-items:flex-start}
.foot-brand{width:232px}
.foot-brand .brand{font-size:12px}
.foot-brand p{font-size:9px;line-height:13px;margin-top:14px;color:#444}
.foot-links{display:flex;gap:22px;font-size:9px;color:#444;margin-top:43px}
.copyright{margin-left:auto;font-size:9px;color:#666;margin-top:43px}
</style>
</head>
<body>

<header class="nav">
  <div class="wrap">
    <div class="brand"><span class="brand-dot"></span>SANDLINE RETREATS</div>
    <nav class="nav-links"><span>The Property</span><span>Amenities</span><span>Availability</span><span>Reviews</span><span>Location</span></nav>
    <span class="btn-book">Book Now</span>
  </div>
</header>

<section class="hero" role="img" aria-label="Sunset over the Gulf with waves rolling onto the beach">
  <div class="hero-copy">
    <h1 class="serif">Your Private Sanctuary on the Sands of Indian Rocks Beach</h1>
    <p>Experience the ultimate Gulf Coast escape in our luxury beachfront duplex, where the sound of the waves is your daily soundtrack.</p>
    <div class="hero-btns"><span class="btn btn-primary">View Availability</span><span class="btn btn-ghost">Explore Gallery</span></div>
  </div>
</section>

<section class="experience">
  <div class="wrap">
    <div class="photo-frame"><div class="photo-interior" role="img" aria-label="Bright living room with sofas facing floor-to-ceiling windows onto the ocean"></div></div>
    <div class="exp-text">
      <div class="eyebrow">THE EXPERIENCE</div>
      <h2 class="serif">Two Units, One Pristine Shoreline</h2>
      <p class="exp-lead">TidehavenDuplex offers a unique architectural experience designed for those who value privacy without sacrificing connection. Our beachfront property is split into two mirrored luxury units, each providing a secluded sanctuary for families or groups.</p>
      <p class="exp-sub">Whether you rent one side for a romantic retreat or the entire duplex for a multi-generational reunion, you'll enjoy expansive floor plans, private outdoor spaces, and direct steps from your door to the warm Gulf sands.</p>
      <ul class="checks">
        <li><svg width="16" height="16" viewBox="0 0 16 16"><circle cx="8" cy="8" r="7" fill="none" stroke="#0b5f96" stroke-width="1.6"/><path d="M4.8 8.2l2.2 2.2 4.2-4.4" fill="none" stroke="#0b5f96" stroke-width="1.6"/></svg>Separate Entrances &amp; Decks</li>
        <li><svg width="16" height="16" viewBox="0 0 16 16"><circle cx="8" cy="8" r="7" fill="none" stroke="#0b5f96" stroke-width="1.6"/><path d="M4.8 8.2l2.2 2.2 4.2-4.4" fill="none" stroke="#0b5f96" stroke-width="1.6"/></svg>Vaulted Ceilings &amp; Ocean Views</li>
        <li><svg width="16" height="16" viewBox="0 0 16 16"><circle cx="8" cy="8" r="7" fill="none" stroke="#0b5f96" stroke-width="1.6"/><path d="M4.8 8.2l2.2 2.2 4.2-4.4" fill="none" stroke="#0b5f96" stroke-width="1.6"/></svg>Seamless Indoor-Outdoor Flow</li>
      </ul>
      <span class="link-floor">Discover the Floorplans <svg width="14" height="10" viewBox="0 0 14 10"><path d="M1 5h11M8 1l4 4-4 4" fill="none" stroke="#0b5f96" stroke-width="1.5"/></svg></span>
    </div>
  </div>
</section>

<section class="curated">
  <div class="wrap">
    <h2 class="serif">Curated for Comfort</h2>
    <p class="intro">Every detail at TidehavenDuplex is thoughtfully chosen to elevate your stay from a simple trip to an unforgettable memory.</p>
    <div class="cards">
      <div class="card">
        <div class="card-icon"><svg width="20" height="20" viewBox="0 0 20 20"><path d="M2 14c3-2 5-2 8 0s5 2 8 0" fill="none" stroke="#fff" stroke-width="1.8"/><circle cx="14" cy="6" r="3" fill="#fff"/></svg></div>
        <h3 class="serif">Direct Beach Access</h3>
        <p>No roads to cross. Walk from your private patio directly onto the soft white sands of the Gulf.</p>
      </div>
      <div class="card">
        <div class="card-icon"><svg width="20" height="20" viewBox="0 0 20 20"><circle cx="8" cy="10" r="5.5" fill="none" stroke="#fff" stroke-width="1.8"/><path d="M13.5 10h5" stroke="#fff" stroke-width="2"/></svg></div>
        <h3 class="serif">Chef's Kitchen</h3>
        <p>Fully equipped with stainless appliances, quartz counters, and everything needed for a seaside feast.</p>
      </div>
      <div class="card">
        <div class="card-icon"><svg width="20" height="20" viewBox="0 0 20 20"><path d="M4 14a6 6 0 0 1 12 0" fill="none" stroke="#fff" stroke-width="1.8"/><path d="M2 16h16" stroke="#fff" stroke-width="1.8"/></svg></div>
        <h3 class="serif">Private Sunset Decks</h3>
        <p>Expansive elevated decks facing West—the perfect front-row seat for Florida's legendary sunsets.</p>
      </div>
    </div>
    <div class="testimonial">
      <svg width="48" height="36" viewBox="0 0 48 36"><path d="M4 34l6-14H4V2h18v18l-6 14zM26 34l6-14h-6V2h18v18l-6 14z" fill="#0b5f96"/></svg>
      <blockquote>"We've stayed at dozens of rentals along the Gulf, but TidehavenDuplex is in a league of its own. The proximity to the water, the quiet elegance of the interior, and the ease of being in IRB made this our best family vacation yet. Waking up to the dolphins every morning was magical."</blockquote>
      <div class="author"><span class="avatar">MH</span><div class="author-text">Maren Holloway<br>Stayed October 2023</div></div>
    </div>
  </div>
</section>

<section class="local">
  <div class="wrap">
    <div class="local-text">
      <h2 class="serif">Indian Rocks Beach: The Heart of Old Florida</h2>
      <p>Step outside and discover IRB—a charming, walkable coastal town that retains its laid-back heritage while offering gourmet dining and boutique shopping.</p>
      <div class="chips"><span class="chip">Walkable Town</span><span class="chip">Local Eateries</span><span class="chip">Peaceful Environment</span></div>
      <span class="local-link">Explore IRB Guide <svg width="14" height="10" viewBox="0 0 14 10"><path d="M1 5h11M8 1l4 4-4 4" fill="none" stroke="#0b5f96" stroke-width="1.5"/></svg></span>
    </div>
    <div class="photo-town" role="img" aria-label="Colorful beach-town shops lined with tall palm trees under a blue sky"></div>
  </div>
</section>

<section class="cta">
  <h2 class="serif">Ready for your Gulf Coast escape?</h2>
  <p>Our calendar for the coming season is filling up fast. Secure your preferred dates at TidehavenDuplex today.</p>
  <div class="cta-btns"><span class="btn-light">Check Real-Time Availability</span><span class="btn-outline">Contact Host</span></div>
</section>

<footer class="footer">
  <div class="wrap">
    <div class="foot-brand">
      <div class="brand"><span class="brand-dot"></span>SANDLINE RETREATS</div>
      <p>Luxury beachfront living on the pristine shores of Indian Rocks Beach, Florida.</p>
    </div>
    <nav class="foot-links"><span>Privacy Policy</span><span>Terms of Service</span><span>Rental Agreement</span><span>Contact Us</span></nav>
    <span class="copyright">© 2024 Indian Rocks Beach Duplex. All rights reserved.</span>
  </div>
</footer>

</body>
</html>
```